Health software company called BRIGHT MERIDIAN, committed to innovation and technological excellence

The powerpoint presentation template is necessary, very necessary is elegant and modern with innovative images and the color palette attached. The presentation will be used for the business plan and investor presentations that we will use to raise funds. Please, recommend a modern typeface, as well as format to be able to use it and incorporate it as part of the company's brand guidelines. Great diversity of technological solutions
Updates

Very low attendance of designers for a high budget. Very few proposals and no capture my interest

Need extra days to review

Need extra days to review

Need extra days to review

Target Market(s)

managers, managers of public and private health centers, government states, investors

Industry/Entity Type

It Company

Font styles to use
Serif

Requirements
Must have
• The powerpoint presentation template is necessary, very necessary is elegant, minimalist and modern with innovative images and the color palette attached. it must be refined in demarcated style
Nice to have
• very nice, visually harmonic avoid saturation
Should not have
• NO dark colors NO dark colors NO dark colors NO dark colors NO dark colors

```html
<!DOCTYPE html>
<html lang="en">
<head>
<meta charset="utf-8">
<title>Bright Meridian — Business Plan Presentation Template</title>
<link href="https://fonts.googleapis.com/css2?family=Montserrat:wght@300;400;600;700&display=swap" rel="stylesheet">
<style>
  :root{
    --cyan:#45e3ee;
    --cyan-soft:#8bf0f3;
    --blue:#2f7ef0;
    --sky:#2aa6ec;
    --title:#2a9fe6;
    --ink:#3a3f47;
    --muted:#9aa1aa;
    --line:#d9dee3;
    --frame:#d4d8dc;
    --page:#ffffff;
    --num:#6b7075;
  }
  *{box-sizing:border-box;margin:0;padding:0}
  html,body{width:1200px;height:1120px;overflow:hidden;background:var(--page)}
  body{font-family:"Montserrat",sans-serif;color:var(--ink)}
  .deck{
    position:relative;width:1200px;height:1120px;padding:8px 0 0 12px;
    display:grid;grid-template-columns:repeat(5,219px);grid-auto-rows:160px;column-gap:20px;
  }
  .cell{position:relative}
  .slide{position:relative;width:219px;height:124px;background:#fff;border:1px solid var(--frame);overflow:hidden}
  .slide svg{position:absolute;inset:0;width:100%;height:100%}
  .num{display:block;margin:5px 0 0 3px;font-size:11px;font-weight:600;color:var(--num)}
  .ttl{font-size:8.5px;fill:var(--title);font-weight:400}
  .sub{font-size:2.6px;fill:var(--muted)}
  .tx{font-size:2.7px;fill:var(--muted)}
  .tb{font-size:2.9px;fill:var(--ink);font-weight:700}
  .tl{font-size:3.6px;fill:var(--ink)}
  .white{fill:#fff}
  .para{position:absolute;font-size:2.7px;line-height:1.4;color:var(--muted);text-align:justify}
  .cols{column-gap:10px}
</style>
</head>
<body>
<svg width="0" height="0" style="position:absolute" aria-hidden="true">
  <defs>
    <linearGradient id="wash" x1="0" y1="0" x2="1" y2="1">
      <stop offset="0" stop-color="#5cf0f6"/>
      <stop offset="1" stop-color="#3a97ef"/>
    </linearGradient>
    <linearGradient id="washSoft" x1="0" y1="0" x2="1" y2="1">
      <stop offset="0" stop-color="#7fe9f3"/>
      <stop offset="1" stop-color="#3e9eea"/>
    </linearGradient>
  </defs>
</svg>

<main class="deck">

  <!-- 1 cover -->
  <div class="cell"><div class="slide"><svg viewBox="0 0 219 124">
    <rect role="img" aria-label="Photo of medical technology workspace in cyan tones" width="219" height="124" fill="url(#wash)"/>
    <circle cx="109.5" cy="38" r="11" fill="none" stroke="#fff" stroke-opacity=".6" stroke-width=".6"/>
    <text x="109.5" y="37" text-anchor="middle" style="font-size:3.4px;fill:#fff;opacity:.75">YOUR</text>
    <text x="109.5" y="41" text-anchor="middle" style="font-size:3.4px;fill:#fff;opacity:.75">LOGO</text>
    <text x="109.5" y="80" text-anchor="middle" style="font-size:10px;font-weight:700" class="white">BUSINESS PLAN</text>
    <line x1="70" y1="85" x2="149" y2="85" stroke="#fff" stroke-width=".5"/>
    <text x="109.5" y="92" text-anchor="middle" style="font-size:4px;fill:#fff;opacity:.85">COMMITTED TO INNOVATION AND</text>
    <text x="109.5" y="97" text-anchor="middle" style="font-size:4px;fill:#fff;opacity:.85">TECHNOLOGICAL EXCELLENCE</text>
  </svg></div><span class="num">1</span></div>

  <!-- 2 welcome -->
  <div class="cell"><div class="slide"><svg viewBox="0 0 219 124">
    <text x="18" y="16" class="ttl">WELCOME</text>
    <circle cx="112" cy="42" r="15" fill="none" stroke="var(--cyan)" stroke-width=".7"/>
    <text x="112" y="68" text-anchor="middle" class="tb" style="font-size:3.2px">FIRST LAST NAME</text>
    <text x="112" y="72" text-anchor="middle" class="tx">PRESIDENT, BRIGHT MERIDIAN</text>
  </svg>
  <p class="para" style="left:20px;top:79px;width:180px">Include a welcome message from your President here. Include a welcome message from your President here. Include a welcome message from your President here. Include a welcome message from your President here. Include a welcome message from your President here. Include a welcome message from your President here. Include a welcome message from your President here. Include a welcome message from your President here. Include a welcome message from your President here. Include a welcome message here.</p>
  </div><span class="num">2</span></div>

  <!-- 3 table of contents -->
  <div class="cell"><div class="slide"><svg viewBox="0 0 219 124">
    <text x="18" y="16" class="ttl">TABLE OF CONTENTS</text>
    <g>
      <text x="89" y="35" text-anchor="end" style="font-size:3px;fill:var(--cyan);font-weight:600">PAGE 1</text>
      <line x1="94" y1="31" x2="94" y2="44" stroke="var(--line)" stroke-width=".4"/>
      <text x="103" y="35" style="font-size:3px;fill:var(--cyan);font-weight:600">Topic Title</text>
      <text x="103" y="39" class="tx">Clarifying text, as necessary should go here in</text>
      <text x="103" y="42" class="tx">this text section.</text>
    </g>
    <g transform="translate(0,21)">
      <text x="89" y="35" text-anchor="end" style="font-size:3px;fill:var(--cyan);font-weight:600">PAGE 2</text>
      <line x1="94" y1="31" x2="94" y2="44" stroke="var(--line)" stroke-width=".4"/>
      <text x="103" y="35" style="font-size:3px;fill:var(--cyan);font-weight:600">Topic Title</text>
      <text x="103" y="39" class="tx">Clarifying text, as necessary should go here in</text>
      <text x="103" y="42" class="tx">this text section.</text>
    </g>
    <g transform="translate(0,42)">
      <text x="89" y="35" text-anchor="end" style="font-size:3px;fill:var(--cyan);font-weight:600">PAGE 3</text>
      <line x1="94" y1="31" x2="94" y2="44" stroke="var(--line)" stroke-width=".4"/>
      <text x="103" y="35" style="font-size:3px;fill:var(--cyan);font-weight:600">Topic Title</text>
      <text x="103" y="39" class="tx">Clarifying text, as necessary should go here in</text>
      <text x="103" y="42" class="tx">this text section.</text>
    </g>
    <g transform="translate(0,63)">
      <text x="89" y="35" text-anchor="end" style="font-size:3px;fill:var(--cyan);font-weight:600">PAGE 4</text>
      <line x1="94" y1="31" x2="94" y2="44" stroke="var(--line)" stroke-width=".4"/>
      <text x="103" y="35" style="font-size:3px;fill:var(--cyan);font-weight:600">Topic Title</text>
      <text x="103" y="39" class="tx">Clarifying text, as necessary should go here in</text>
      <text x="103" y="42" class="tx">this text section.</text>
    </g>
  </svg></div><span class="num">3</span></div>

  <!-- 4 agenda -->
  <div class="cell"><div class="slide"><svg viewBox="0 0 219 124">
    <text x="18" y="16" class="ttl">AGENDA</text>
    <g>
      <text x="89" y="35" text-anchor="end" class="tb" style="font-size:3px">9:00am-10:00am</text>
      <line x1="94" y1="31" x2="94" y2="44" stroke="var(--line)" stroke-width=".4"/>
      <text x="103" y="35" class="tb" style="font-size:3px">Topic Title</text>
      <text x="103" y="39" class="tx">Clarifying text, as necessary should go here in</text>
      <text x="103" y="42" class="tx">this text section.</text>
    </g>
    <g transform="translate(0,21)">
      <text x="89" y="35" text-anchor="end" class="tb" style="font-size:3px">10:00am-11:00am</text>
      <line x1="94" y1="31" x2="94" y2="44" stroke="var(--line)" stroke-width=".4"/>
      <text x="103" y="35" class="tb" style="font-size:3px">Topic Title</text>
      <text x="103" y="39" class="tx">Clarifying text, as necessary should go here in</text>
      <text x="103" y="42" class="tx">this text section.</text>
    </g>
    <g transform="translate(0,42)">
      <text x="89" y="35" text-anchor="end" class="tb" style="font-size:3px">11:00am-12:00pm</text>
      <line x1="94" y1="31" x2="94" y2="44" stroke="var(--line)" stroke-width=".4"/>
      <text x="103" y="35" class="tb" style="font-size:3px">Topic Title</text>
      <text x="103" y="39" class="tx">Clarifying text, as necessary should go here in</text>
      <text x="103" y="42" class="tx">this text section.</text>
    </g>
    <g transform="translate(0,63)">
      <text x="89" y="35" text-anchor="end" class="tb" style="font-size:3px">12:00pm-1:00pm</text>
      <line x1="94" y1="31" x2="94" y2="44" stroke="var(--line)" stroke-width=".4"/>
      <text x="103" y="35" class="tb" style="font-size:3px">Topic Title</text>
      <text x="103" y="39" class="tx">Clarifying text, as necessary should go here in</text>
      <text x="103" y="42" class="tx">this text section.</text>
    </g>
  </svg></div><span class="num">4</span></div>

  <!-- 5 mission vision value -->
  <div class="cell"><div class="slide"><svg viewBox="0 0 219 124">
    <text x="18" y="16" class="ttl">MISSION, VISION, VALUE</text>
    <text x="18" y="22" class="sub">Add some summary text here to reinforce your points.</text>
    <line x1="73" y1="58" x2="91" y2="58" stroke="var(--cyan)" stroke-width=".5"/>
    <line x1="129" y1="58" x2="146" y2="58" stroke="var(--cyan)" stroke-width=".5"/>
    <circle cx="54" cy="58" r="19" fill="none" stroke="var(--cyan)" stroke-width=".9"/>
    <circle cx="110" cy="58" r="19" fill="none" stroke="var(--cyan)" stroke-width=".9"/>
    <circle cx="165" cy="58" r="19" fill="none" stroke="var(--blue)" stroke-width=".9"/>
    <text x="54" y="59" text-anchor="middle" class="tb" style="font-size:3px">MISSION</text>
    <text x="110" y="59" text-anchor="middle" class="tb" style="font-size:3px">VISION</text>
    <text x="165" y="59" text-anchor="middle" class="tb" style="font-size:3px">VALUE</text>
    <g class="tx" text-anchor="middle">
      <text x="54" y="93">Refers to a good or service</text><text x="54" y="96.5">being offered by a</text><text x="54" y="100">company. Ideally, a</text><text x="54" y="103.5">product should meet a</text><text x="54" y="107">certain consumer demand</text>
      <text x="110" y="93">Refers to a good or service</text><text x="110" y="96.5">being offered by a</text><text x="110" y="100">company. Ideally, a</text><text x="110" y="103.5">product should meet a</text><text x="110" y="107">certain consumer demand</text>
      <text x="165" y="93">Refers to a good or service</text><text x="165" y="96.5">being offered by a</text><text x="165" y="100">company. Ideally, a</text><text x="165" y="103.5">product should meet a</text><text x="165" y="107">certain consumer demand</text>
    </g>
  </svg></div><span class="num">5</span></div>

  <!-- 6 market research -->
  <div class="cell"><div class="slide"><svg viewBox="0 0 219 124">
    <text x="18" y="21" class="ttl">MARKET RESEARCH</text>
    <text x="18" y="27" class="sub">Add some summary text here to reinforce your points.</text>
    <g fill="none" stroke-width="4">
      <circle cx="44" cy="72" r="21" stroke="#eeeff1"/>
      <circle cx="44" cy="72" r="21" stroke="var(--cyan)" stroke-dasharray="59.4 132" transform="rotate(-90 44 72)"/>
      <circle cx="111" cy="72" r="21" stroke="#eeeff1"/>
      <circle cx="111" cy="72" r="21" stroke="var(--blue)" stroke-dasharray="59.4 132" transform="rotate(-90 111 72)"/>
      <circle cx="178" cy="72" r="21" stroke="#eeeff1"/>
      <circle cx="178" cy="72" r="21" stroke="var(--cyan)" stroke-dasharray="99 132" transform="rotate(-90 178 72)"/>
    </g>
    <g text-anchor="middle">
      <text x="44" y="67" class="tl" style="font-size:5px">45%</text>
      <text x="44" y="72" class="tx">of the</text><text x="44" y="75.5" class="tx">market is</text><text x="44" y="79" class="tx">something</text><text x="44" y="82.5" class="tx">meaningful</text>
      <text x="111" y="67" class="tl" style="font-size:5px">45%</text>
      <text x="111" y="72" class="tx">of the</text><text x="111" y="75.5" class="tx">market is</text><text x="111" y="79" class="tx">something</text><text x="111" y="82.5" class="tx">meaningful</text>
      <text x="178" y="67" class="tl" style="font-size:5px">75%</text>
      <text x="178" y="72" class="tx">of the</text><text x="178" y="75.5" class="tx">market is</text><text x="178" y="79" class="tx">something</text><text x="178" y="82.5" class="tx">meaningful</text>
    </g>
  </svg></div><span class="num">6</span></div>

  <!-- 7 market research quote -->
  <div class="cell"><div class="slide"><svg viewBox="0 0 219 124">
    <rect role="img" aria-label="Soft photo of digital health interface in cyan and blue" width="219" height="124" fill="url(#washSoft)"/>
    <text x="109.5" y="52" text-anchor="middle" style="font-size:7.4px;font-weight:700" class="white">MARKET RESEARCH QUOTE</text>
    <text x="109.5" y="74" text-anchor="middle" style="font-size:3.8px;fill:#fff;opacity:.85">A PRODUCT LIKE THIS IS SO IMPORTANT TO ME. IT</text>
    <text x="109.5" y="79" text-anchor="middle" style="font-size:3.8px;fill:#fff;opacity:.85">WILL HELP ME ACHIEVE X, Y, Z.</text>
    <text x="109.5" y="90" text-anchor="middle" style="font-size:2.6px;fill:#fff;opacity:.8">NAME COMPANY</text>
  </svg></div><span class="num">7</span></div>

  <!-- 8 important statement -->
  <div class="cell"><div class="slide"><svg viewBox="0 0 219 124">
    <rect role="img" aria-label="Photo band of medical data screens in cyan tones" width="219" height="58" fill="url(#wash)"/>
    <text x="109.5" y="42" text-anchor="middle" style="font-size:8px;font-weight:700" class="white">IMPORTANT STATEMENT</text>
    <line x1="73" y1="68" x2="73" y2="118" stroke="var(--line)" stroke-width=".4"/>
    <line x1="146" y1="68" x2="146" y2="118" stroke="var(--line)" stroke-width=".4"/>
    <g text-anchor="middle">
      <text x="37" y="86" style="font-size:6.5px;font-weight:700;fill:var(--sky)">45%</text>
      <text x="109.5" y="86" style="font-size:6.5px;font-weight:700;fill:var(--sky)">25%</text>
      <text x="182" y="86" style="font-size:6.5px;font-weight:700;fill:var(--sky)">77%</text>
      <text x="37" y="100" class="tx">of the market is</text><text x="37" y="103.5" class="tx">something</text><text x="37" y="107" class="tx">meaningful</text>
      <text x="109.5" y="100" class="tx">of the market is</text><text x="109.5" y="103.5" class="tx">something</text><text x="109.5" y="107" class="tx">meaningful</text>
      <text x="182" y="100" class="tx">of the market is</text><text x="182" y="103.5" class="tx">something</text><text x="182" y="107" class="tx">meaningful</text>
    </g>
  </svg></div><span class="num">8</span></div>

  <!-- 9 business model -->
  <div class="cell"><div class="slide"><svg viewBox="0 0 219 124">
    <text x="18" y="17" class="ttl">BUSINESS MODEL</text>
    <text x="18" y="23" class="sub">Add some summary text here to reinforce your points.</text>
    <polygon points="12,50 80,50 84,54 80,58 12,58" fill="var(--cyan)"/>
    <polygon points="80,50 144,50 148,54 144,58 80,58 84,54" fill="var(--blue)"/>
    <polygon points="144,50 203,50 207,54 203,58 144,58 148,54" fill="var(--cyan-soft)"/>
    <g text-anchor="middle" style="font-size:3px;font-weight:600" class="white">
      <text x="47" y="55.2">Customers</text><text x="113" y="55.2">Payment Structure</text><text x="176" y="55.2">Retention</text>
    </g>
  </svg>
  <p class="para" style="left:15px;top:67px;width:56px">Add some summary text here to reinforce your points. Add some summary text here to reinforce your points. Add some summary text here to reinforce your points.</p>
  <p class="para" style="left:81px;top:67px;width:56px">Add some summary text here to reinforce your points. Add some summary text here to reinforce your points. Add some summary text here to reinforce your points.</p>
  <p class="para" style="left:147px;top:67px;width:56px">Add some summary text here to reinforce your points. Add some summary text here to reinforce your points. Add some summary text here to reinforce your points.</p>
  </div><span class="num">9</span></div>

  <!-- 10 product features -->
  <div class="cell"><div class="slide"><svg viewBox="0 0 219 124">
    <text x="18" y="17" class="ttl">PRODUCT FEATURES</text>
    <text x="18" y="23" class="sub">Add some summary text here to reinforce your points.</text>
    <circle cx="38" cy="43" r="9" fill="var(--cyan)"/>
    <circle cx="84" cy="43" r="9" fill="var(--cyan)"/>
    <circle cx="130" cy="43" r="9" fill="var(--blue)"/>
    <circle cx="176" cy="43" r="9" fill="var(--cyan-soft)"/>
    <g fill="none" stroke="#fff" stroke-width=".9" stroke-linecap="round">
      <rect x="34" y="39" width="8" height="8" rx="1"/><path d="M36.5 41v4M39.5 41v4M36.5 43h3"/>
      <path d="M80 47l1-3 5-5 2 2-5 5z"/>
      <path d="M127 39v3a3 3 0 0 0 6 0v-3M130 45v2a2.5 2.5 0 0 0 5 0v-1"/>
      <path d="M172 46l8-6-3 8-1.5-2.5z"/>
    </g>
    <g text-anchor="middle">
      <text x="38" y="58" class="tb" style="font-size:2.5px">FEATURE 1</text>
      <text x="84" y="58" class="tb" style="font-size:2.5px">FEATURE 2</text>
      <text x="130" y="58" class="tb" style="font-size:2.5px">FEATURE 3</text>
      <text x="176" y="58" class="tb" style="font-size:2.5px">FEATURE 4</text>
      <text x="38" y="62" class="tx">A little bit of</text><text x="38" y="65" class="tx">context about</text><text x="38" y="68" class="tx">this feature.</text>
      <text x="84" y="62" class="tx">A little bit of</text><text x="84" y="65" class="tx">context about</text><text x="84" y="68" class="tx">this feature.</text>
      <text x="130" y="62" class="tx">A little bit of</text><text x="130" y="65" class="tx">context about</text><text x="130" y="68" class="tx">this feature.</text>
      <text x="176" y="62" class="tx">A little bit of</text><text x="176" y="65" class="tx">context about</text><text x="176" y="68" class="tx">this feature.</text>
    </g>
    <rect role="img" aria-label="Photo of clinicians using a tablet, blue tones" y="76" width="219" height="48" fill="url(#wash)"/>
  </svg></div><span class="num">10</span></div>

  <!-- 11 product timeline -->
  <div class="cell"><div class="slide"><svg viewBox="0 0 219 124">
    <text x="18" y="16" class="ttl">PRODUCT</text>
    <line x1="110" y1="58" x2="110" y2="71" stroke="var(--blue)" stroke-width=".5"/>
    <line x1="45" y1="76" x2="45" y2="89" stroke="var(--cyan)" stroke-width=".5"/>
    <line x1="176" y1="76" x2="176" y2="89" stroke="var(--cyan-soft)" stroke-width=".5"/>
    <polygon points="10,71 93,71 95,73.5 93,76 10,76" fill="var(--cyan)"/>
    <polygon points="93,71 148,71 150,73.5 148,76 93,76 95,73.5" fill="var(--blue)"/>
    <polygon points="148,71 212,71 214,73.5 212,76 148,76 150,73.5" fill="var(--cyan-soft)"/>
    <g text-anchor="middle" style="font-size:2.8px;font-weight:600" class="white">
      <text x="45" y="74.6">2018</text><text x="120" y="74.6">2019</text><text x="180" y="74.6">2020</text>
    </g>
    <circle cx="110" cy="45" r="13" fill="#fff" stroke="var(--blue)" stroke-width=".8"/>
    <circle cx="45" cy="102" r="13" fill="#fff" stroke="var(--cyan)" stroke-width=".8"/>
    <circle cx="176" cy="102" r="13" fill="#fff" stroke="var(--cyan-soft)" stroke-width=".8"/>
    <g text-anchor="middle" class="tb" style="font-size:2.2px">
      <text x="110" y="44.5">PRODUCT</text><text x="110" y="47.3">NAME</text>
      <text x="45" y="101.5">PRODUCT</text><text x="45" y="104.3">NAME</text>
      <text x="176" y="101.5">PRODUCT</text><text x="176" y="104.3">NAME</text>
    </g>
  </svg></div><span class="num">11</span></div>

  <!-- 12 product zigzag -->
  <div class="cell"><div class="slide"><svg viewBox="0 0 219 124">
    <text x="18" y="16" class="ttl">PRODUCT</text>
    <polyline points="0,72 38,38 74,102 110,38 147,102 184,38 219,72" fill="none" stroke="var(--line)" stroke-width=".5"/>
    <g class="tx" text-anchor="middle" style="font-size:2.4px">
      <text x="38" y="72">2017</text><text x="74" y="72">2017</text><text x="110" y="72">2017</text><text x="147" y="72">2017</text><text x="184" y="72">2017</text>
    </g>
    <circle cx="38" cy="38" r="12" fill="#fff" stroke="var(--cyan)" stroke-width=".8"/>
    <circle cx="74" cy="102" r="12" fill="#fff" stroke="var(--cyan)" stroke-width=".8"/>
    <circle cx="110" cy="38" r="12" fill="#fff" stroke="var(--blue)" stroke-width=".8"/>
    <circle cx="147" cy="102" r="12" fill="#fff" stroke="var(--blue)" stroke-width=".8"/>
    <circle cx="184" cy="38" r="12" fill="#fff" stroke="var(--cyan-soft)" stroke-width=".8"/>
    <g text-anchor="middle" class="tb" style="font-size:2.2px">
      <text x="38" y="37.5">PRODUCT</text><text x="38" y="40.3">NAME</text>
      <text x="74" y="101.5">PRODUCT</text><text x="74" y="104.3">NAME</text>
      <text x="110" y="37.5">PRODUCT</text><text x="110" y="40.3">NAME</text>
      <text x="147" y="101.5">PRODUCT</text><text x="147" y="104.3">NAME</text>
      <text x="184" y="37.5">PRODUCT</text><text x="184" y="40.3">NAME</text>
    </g>
  </svg></div><span class="num">12</span></div>

  <!-- 13 product steps -->
  <div class="cell"><div class="slide"><svg viewBox="0 0 219 124">
    <text x="18" y="16" class="ttl">PRODUCT</text>
    <line x1="18" y1="72" x2="200" y2="72" stroke="var(--line)" stroke-width=".5"/>
    <circle cx="35" cy="38" r="4.5" fill="var(--blue)"/>
    <circle cx="109" cy="38" r="4.5" fill="var(--cyan)"/>
    <circle cx="184" cy="38" r="4.5" fill="var(--cyan)"/>
    <circle cx="72" cy="82" r="4.5" fill="var(--cyan)"/>
    <circle cx="147" cy="82" r="4.5" fill="var(--blue)"/>
    <g text-anchor="middle" style="font-size:3.6px;font-weight:600" class="white">
      <text x="35" y="39.3">1</text><text x="109" y="39.3">3</text><text x="184" y="39.3">5</text><text x="72" y="83.3">2</text><text x="147" y="83.3">4</text>
    </g>
    <g text-anchor="middle">
      <text x="35" y="49" class="tb" style="font-size:2.8px">TITLE</text><text x="35" y="52.5" class="tx">Write here</text><text x="35" y="55.5" class="tx">something about</text>
      <text x="109" y="49" class="tb" style="font-size:2.8px">TITLE</text><text x="109" y="52.5" class="tx">Write here</text><text x="109" y="55.5" class="tx">something about</text>
      <text x="184" y="49" class="tb" style="font-size:2.8px">TITLE</text><text x="184" y="52.5" class="tx">Write here</text><text x="184" y="55.5" class="tx">something about</text>
      <text x="72" y="93" class="tb" style="font-size:2.8px">TITLE</text><text x="72" y="96.5" class="tx">Write here</text><text x="72" y="99.5" class="tx">something about</text>
      <text x="147" y="93" class="tb" style="font-size:2.8px">TITLE</text><text x="147" y="96.5" class="tx">Write here</text><text x="147" y="99.5" class="tx">something about</text>
    </g>
  </svg></div><span class="num">13</span></div>

  <!-- 14 target public -->
  <div class="cell"><div class="slide"><svg viewBox="0 0 219 124">
    <text x="14" y="16" class="ttl">TARGET PUBLIC</text>
    <text x="14" y="22" class="sub">Add some summary text here to</text>
    <text x="14" y="25" class="sub">reinforce your points.</text>
    <g style="font-size:4.2px;fill:var(--cyan);font-weight:600">
      <text x="25" y="45">1</text><text x="25" y="65">2</text><text x="25" y="87">3</text><text x="25" y="108">4</text>
    </g>
    <g stroke="var(--line)" stroke-width=".4">
      <line x1="30" y1="40" x2="30" y2="46"/><line x1="30" y1="60" x2="30" y2="66"/><line x1="30" y1="82" x2="30" y2="88"/><line x1="30" y1="103" x2="30" y2="109"/>
    </g>
    <g class="tl" style="font-size:3.4px">
      <text x="34" y="44.5">Target public #1</text><text x="34" y="64.5">Target public #2</text><text x="34" y="86.5">Target public #3</text><text x="34" y="107.5">Target public #4</text>
    </g>
    <rect role="img" aria-label="Photo of a doctor holding a tablet, cyan-blue tones" x="118" width="101" height="124" fill="url(#washSoft)"/>
  </svg></div><span class="num">14</span></div>

  <!-- 15 list of 4 items -->
  <div class="cell"><div class="slide"><svg viewBox="0 0 219 124">
    <rect role="img" aria-label="Photo of medical team with digital overlay, cyan-blue tones" width="96" height="124" fill="url(#washSoft)"/>
    <text x="115" y="16" class="ttl" style="font-size:7.5px">LIST OF 4 ITEMS</text>
    <text x="115" y="22" class="sub">Add some summary text here to</text>
    <text x="115" y="25" class="sub">reinforce your points.</text>
    <g style="font-size:4.2px;fill:var(--cyan);font-weight:600">
      <text x="119" y="46">1</text><text x="119" y="67">2</text><text x="119" y="88">3</text><text x="119" y="109">4</text>
    </g>
    <g stroke="var(--line)" stroke-width=".4">
      <line x1="124" y1="40" x2="124" y2="48"/><line x1="124" y1="61" x2="124" y2="69"/><line x1="124" y1="82" x2="124" y2="90"/><line x1="124" y1="103" x2="124" y2="111"/>
    </g>
    <g class="tx">
      <text x="128" y="43">Add some summary text here to</text><text x="128" y="46.5">reinforce your points.</text>
      <text x="128" y="64">Add some summary text here to</text><text x="128" y="67.5">reinforce your points.</text>
      <text x="128" y="85">Add some summary text here to</text><text x="128" y="88.5">reinforce your points.</text>
      <text x="128" y="106">Add some summary text here to</text><text x="128" y="109.5">reinforce your points.</text>
    </g>
  </svg></div><span class="num">15</span></div>

  <!-- 16 list of 8 items -->
  <div class="cell"><div class="slide"><svg viewBox="0 0 219 124">
    <text x="18" y="16" class="ttl" style="font-size:7.5px">LIST OF 8 ITEMS</text>
    <text x="18" y="22" class="sub">Add some summary text here to reinforce your points.</text>
    <g style="font-size:4.2px;fill:var(--cyan);font-weight:600">
      <text x="22" y="43">1</text><text x="22" y="64">2</text><text x="22" y="85">3</text><text x="22" y="106">4</text>
      <text x="122" y="43">5</text><text x="122" y="64">6</text><text x="122" y="85">7</text><text x="122" y="106">8</text>
    </g>
    <g stroke="var(--line)" stroke-width=".4">
      <line x1="27" y1="37" x2="27" y2="47"/><line x1="27" y1="58" x2="27" y2="68"/><line x1="27" y1="79" x2="27" y2="89"/><line x1="27" y1="100" x2="27" y2="110"/>
      <line x1="127" y1="37" x2="127" y2="47"/><line x1="127" y1="58" x2="127" y2="68"/><line x1="127" y1="79" x2="127" y2="89"/><line x1="127" y1="100" x2="127" y2="110"/>
    </g>
    <g>
      <text x="31" y="39" class="tb" style="font-size:2.7px">POINT 1</text><text x="31" y="42.5" class="tx">Add some summary text here</text><text x="31" y="46" class="tx">to reinforce your points.</text>
      <text x="31" y="60" class="tb" style="font-size:2.7px">POINT 2</text><text x="31" y="63.5" class="tx">Add some summary text here</text><text x="31" y="67" class="tx">to reinforce your points.</text>
      <text x="31" y="81" class="tb" style="font-size:2.7px">POINT 3</text><text x="31" y="84.5" class="tx">Add some summary text here</text><text x="31" y="88" class="tx">to reinforce your points.</text>
      <text x="31" y="102" class="tb" style="font-size:2.7px">POINT 4</text><text x="31" y="105.5" class="tx">Add some summary text here</text><text x="31" y="109" class="tx">to reinforce your points.</text>
      <text x="131" y="39" class="tb" style="font-size:2.7px">POINT 5</text><text x="131" y="42.5" class="tx">Add some summary text here</text><text x="131" y="46" class="tx">to reinforce your points.</text>
      <text x="131" y="60" class="tb" style="font-size:2.7px">POINT 6</text><text x="131" y="63.5" class="tx">Add some summary text here</text><text x="131" y="67" class="tx">to reinforce your points.</text>
      <text x="131" y="81" class="tb" style="font-size:2.7px">POINT 7</text><text x="131" y="84.5" class="tx">Add some summary text here</text><text x="131" y="88" class="tx">to reinforce your points.</text>
      <text x="131" y="102" class="tb" style="font-size:2.7px">POINT 8</text><text x="131" y="105.5" class="tx">Add some summary text here</text><text x="131" y="109" class="tx">to reinforce your points.</text>
    </g>
  </svg></div><span class="num">16</span></div>

  <!-- 17 our services -->
  <div class="cell"><div class="slide"><svg viewBox="0 0 219 124">
    <text x="18" y="16" class="ttl" style="font-size:7.5px">OUR SERVICES</text>
    <text x="18" y="22" class="sub">Add some summary text here to reinforce your points.</text>
    <g fill="none" stroke-width="1" stroke-linecap="round" stroke-linejoin="round">
      <path d="M29 48l6-6M35 42a2.5 2.5 0 1 0 2-3" stroke="var(--cyan)"/>
      <rect x="78" y="40" width="6" height="8" rx="1" stroke="var(--cyan)"/>
      <rect x="124" y="40" width="9" height="6" rx=".5" stroke="var(--blue)"/><path d="M122 48h13" stroke="var(--blue)"/>
      <path d="M173 48l2-4 5-5 1 2-5 5z" stroke="var(--sky)"/>
      <path d="M29 80v5c0 2 4 3 4 3s4-1 4-3v-5l-4-1.5z" stroke="var(--blue)"/>
      <path d="M76 83l5-2.5 5 2.5-5 2.5zM78.5 84.5v2.5c1.5 1 3.5 1 5 0v-2.5" stroke="var(--cyan)"/>
      <circle cx="129" cy="84" r="4" stroke="var(--cyan)"/>
      <path d="M174 80v3a3 3 0 0 0 6 0v-3M177 86v1.5a2.5 2.5 0 0 0 5 0v-1" stroke="var(--blue)"/>
    </g>
    <g text-anchor="middle">
      <text x="33" y="57" class="tb" style="font-size:2.3px">SERVICE 1</text><text x="33" y="60" class="tx">Add some summary</text><text x="33" y="63" class="tx">text to reinforce</text>
      <text x="81" y="57" class="tb" style="font-size:2.3px">SERVICE 2</text><text x="81" y="60" class="tx">Add some summary</text><text x="81" y="63" class="tx">text to reinforce</text>
      <text x="129" y="57" class="tb" style="font-size:2.3px">SERVICE 3</text><text x="129" y="60" class="tx">Add some summary</text><text x="129" y="63" class="tx">text to reinforce</text>
      <text x="177" y="57" class="tb" style="font-size:2.3px">SERVICE 4</text><text x="177" y="60" class="tx">Add some summary</text><text x="177" y="63" class="tx">text to reinforce</text>
      <text x="33" y="96" class="tb" style="font-size:2.3px">SERVICE 5</text><text x="33" y="99" class="tx">Add some summary</text><text x="33" y="102" class="tx">text to reinforce</text>
      <text x="81" y="96" class="tb" style="font-size:2.3px">SERVICE 6</text><text x="81" y="99" class="tx">Add some summary</text><text x="81" y="102" class="tx">text to reinforce</text>
      <text x="129" y="96" class="tb" style="font-size:2.3px">SERVICE 7</text><text x="129" y="99" class="tx">Add some summary</text><text x="129" y="102" class="tx">text to reinforce</text>
      <text x="177" y="96" class="tb" style="font-size:2.3px">SERVICE 8</text><text x="177" y="99" class="tx">Add some summary</text><text x="177" y="102" class="tx">text to reinforce</text>
    </g>
  </svg></div><span class="num">17</span></div>

  <!-- 18 pie chart -->
  <div class="cell"><div class="slide"><svg viewBox="0 0 219 124">
    <text x="18" y="21" class="ttl">PIE CHART</text>
    <g style="font-size:5.4px;fill:#6e747c">
      <text x="30" y="50">Make a great</text><text x="30" y="57">point about the</text><text x="30" y="64">data represented</text><text x="30" y="71">in the enclosed</text><text x="30" y="78">pie chart here.</text>
    </g>
    <g fill="none" stroke-width="8">
      <circle cx="150" cy="65" r="27" stroke="var(--cyan)"/>
      <circle cx="150" cy="65" r="27" stroke="var(--cyan-soft)" stroke-dasharray="22 170" transform="rotate(-90 150 65)"/>
      <circle cx="150" cy="65" r="27" stroke="var(--sky)" stroke-dasharray="4 170" transform="rotate(-8 150 65)"/>
    </g>
    <text x="150" y="66" text-anchor="middle" class="tb" style="font-size:2.8px">CHART TITLE</text>
    <g class="tx" style="font-size:2.4px">
      <text x="118" y="107">● 1st Qtr</text><text x="133" y="107">● 2nd Qtr</text><text x="149" y="107">● 3rd Qtr</text><text x="165" y="107">● 4th Qtr</text>
    </g>
  </svg></div><span class="num">18</span></div>

  <!-- 19 bar chart -->
  <div class="cell"><div class="slide"><svg viewBox="0 0 219 124">
    <text x="18" y="21" class="ttl">BAR CHART</text>
    <line x1="40" y1="92" x2="190" y2="92" stroke="var(--line)" stroke-width=".4"/>
    <g>
      <rect x="45" y="58" width="5" height="34" fill="var(--cyan)"/><rect x="51" y="60" width="5" height="32" fill="var(--cyan-soft)"/><rect x="57" y="84" width="5" height="8" fill="var(--blue)"/>
      <rect x="83" y="83" width="5" height="9" fill="var(--cyan)"/><rect x="89" y="83" width="5" height="9" fill="var(--cyan-soft)"/><rect x="95" y="85" width="5" height="7" fill="var(--blue)"/>
      <rect x="121" y="86" width="5" height="6" fill="var(--cyan)"/><rect x="127" y="81" width="5" height="11" fill="var(--cyan-soft)"/><rect x="133" y="55" width="5" height="37" fill="var(--blue)"/>
      <rect x="159" y="86" width="5" height="6" fill="var(--cyan)"/><rect x="165" y="61" width="5" height="31" fill="var(--cyan-soft)"/><rect x="171" y="59" width="5" height="33" fill="var(--blue)"/>
    </g>
    <g class="tx" text-anchor="middle" style="font-size:2.3px">
      <text x="53" y="97">1st Qtr</text><text x="91" y="97">2nd Qtr</text><text x="129" y="97">3rd Qtr</text><text x="167" y="97">4th Qtr</text>
      <text x="115" y="102">● Series1   ● Series2   ● Series3</text>
    </g>
  </svg></div><span class="num">19</span></div>

  <!-- 20 strategy -->
  <div class="cell"><div class="slide"><svg viewBox="0 0 219 124">
    <text x="18" y="21" class="ttl">STRATEGY</text>
    <text x="18" y="27" class="sub">Add some summary text here to reinforce your points.</text>
    <path d="M77 44 Q104 72 77 100" fill="none" stroke="var(--line)" stroke-width=".5"/>
    <rect x="0" y="62" width="70" height="20" fill="var(--cyan)"/>
    <text x="11" y="73.5" style="font-size:3.6px;font-weight:700" class="white">STRATEGY</text>
    <circle cx="71" cy="72" r="8" fill="#fff" stroke="var(--blue)" stroke-width=".8"/>
    <circle cx="71" cy="72" r="3" fill="none" stroke="var(--blue)" stroke-width=".8"/>
    <circle cx="80" cy="44" r="2.5" fill="var(--cyan)"/>
    <circle cx="97" cy="72" r="2.5" fill="var(--cyan)"/>
    <circle cx="80" cy="100" r="2.5" fill="var(--cyan)"/>
    <text x="87" y="44" class="tl" style="font-size:3.4px">STRATEGIC OBJECTIVE 1</text>
    <text x="87" y="48" class="tx">Add a little clarifying text here. It doesn't have to be</text>
    <text x="104" y="72" class="tl" style="font-size:3.4px">STRATEGIC OBJECTIVE 2</text>
    <text x="104" y="76" class="tx">Add a little clarifying text here. It doesn't</text>
    <text x="87" y="100" class="tl" style="font-size:3.4px">STRATEGIC OBJECTIVE 3</text>
    <text x="87" y="104" class="tx">Add a little clarifying text here. It doesn't have to be</text>
  </svg></div><span class="num">20</span></div>

  <!-- 21 financing -->
  <div class="cell"><div class="slide"><svg viewBox="0 0 219 124">
    <text x="18" y="17" class="ttl">FINANCING</text>
    <text x="18" y="23" class="sub">Add some summary text here to reinforce your points.</text>
    <rect x="3" y="32" width="107" height="78" fill="var(--blue)"/>
    <text x="56" y="71" text-anchor="middle" style="font-size:14px;font-weight:700" class="white">$1M</text>
    <text x="56" y="80" text-anchor="middle" style="font-size:5px" class="white">EQUITY FINANCING</text>
    <text x="56" y="86" text-anchor="middle" style="font-size:4.5px" class="white">15%</text>
    <g style="font-size:4.2px;fill:var(--cyan);font-weight:600">
      <text x="126" y="42">1</text><text x="126" y="63">2</text><text x="126" y="84">3</text><text x="126" y="105">4</text>
    </g>
    <g stroke="var(--line)" stroke-width=".4">
      <line x1="131" y1="35" x2="131" y2="45"/><line x1="131" y1="56" x2="131" y2="66"/><line x1="131" y1="77" x2="131" y2="87"/><line x1="131" y1="98" x2="131" y2="108"/>
    </g>
    <g>
      <text x="135" y="37" class="tb" style="font-size:2.7px">USE OF FUNDING 1</text><text x="135" y="40.5" class="tx">Add some summary text here</text><text x="135" y="44" class="tx">to reinforce your points.</text>
      <text x="135" y="58" class="tb" style="font-size:2.7px">USE OF FUNDING 2</text><text x="135" y="61.5" class="tx">Add some summary text here</text><text x="135" y="65" class="tx">to reinforce your points.</text>
      <text x="135" y="79" class="tb" style="font-size:2.7px">USE OF FUNDING 3</text><text x="135" y="82.5" class="tx">Add some summary text here</text><text x="135" y="86" class="tx">to reinforce your points.</text>
      <text x="135" y="100" class="tb" style="font-size:2.7px">USE OF FUNDING 4</text><text x="135" y="103.5" class="tx">Add some summary text here</text><text x="135" y="107" class="tx">to reinforce your points.</text>
    </g>
  </svg></div><span class="num">21</span></div>

  <!-- 22 exit & returns -->
  <div class="cell"><div class="slide"><svg viewBox="0 0 219 124">
    <text x="18" y="20" class="ttl">EXIT &amp; RETURNS</text>
    <text x="18" y="26" class="sub">Add some summary text here to reinforce your points.</text>
    <rect x="18" y="39" width="183" height="8" fill="var(--blue)"/>
    <g class="white" text-anchor="middle" style="font-size:2.1px;font-weight:700">
      <text x="31" y="43.8">SHAREHOLDER</text><text x="56" y="43.8">SHARES</text>
      <text x="82" y="42.5">PRE-MONEY</text><text x="82" y="45.3">VALUATION</text>
      <text x="107" y="42.5">POST-MONEY</text><text x="107" y="45.3">VALUATION</text>
      <text x="133" y="42.5">RETURN AT</text><text x="133" y="45.3">2X</text>
      <text x="158" y="42.5">RETURN AT</text><text x="158" y="45.3">5X</text>
      <text x="184" y="42.5">RETURN AT</text><text x="184" y="45.3">10X</text>
    </g>
    <g stroke="#fff" stroke-width=".4"><line x1="44" y1="39" x2="44" y2="47"/><line x1="69" y1="39" x2="69" y2="47"/><line x1="95" y1="39" x2="95" y2="47"/><line x1="120" y1="39" x2="120" y2="47"/><line x1="146" y1="39" x2="146" y2="47"/><line x1="171" y1="39" x2="171" y2="47"/></g>
    <g fill="#f3f5f7"><rect x="18" y="47" width="183" height="10"/><rect x="18" y="67" width="183" height="10"/><rect x="18" y="87" width="183" height="10"/></g>
    <g class="tx" style="font-size:2.4px">
      <text x="21" y="53">NAME 1</text><text x="21" y="63">NAME 2</text><text x="21" y="73">NAME 3</text><text x="21" y="83">NAME 4</text><text x="21" y="93">NAME 5</text><text x="21" y="103">NAME 6</text>
    </g>
  </svg></div><span class="num">22</span></div>

  <!-- 23 swot -->
  <div class="cell"><div class="slide"><svg viewBox="0 0 219 124">
    <text x="14" y="16" class="ttl">SWOT ANALYSIS</text>
    <circle cx="38" cy="46" r="9" fill="var(--cyan)"/>
    <circle cx="86" cy="46" r="9" fill="var(--cyan)"/>
    <circle cx="133" cy="46" r="9" fill="var(--blue)"/>
    <circle cx="181" cy="46" r="9" fill="var(--cyan-soft)"/>
    <g class="white" text-anchor="middle" style="font-size:8px;font-weight:600">
      <text x="38" y="49">S</text><text x="86" y="49">W</text><text x="133" y="49">O</text><text x="181" y="49">T</text>
    </g>
    <g text-anchor="middle" class="tb" style="font-size:2.7px">
      <text x="38" y="68">STRENGTHS</text><text x="86" y="68">WEAKNESSES</text><text x="133" y="68">OPPORTUNITIES</text><text x="181" y="68">THREATS</text>
    </g>
    <g class="tx" style="font-size:2.6px">
      <text x="26" y="73">•  Strength 1</text><text x="26" y="76.5">•  Strength 2</text><text x="26" y="80">•  Strength 3</text><text x="26" y="83.5">•  Strength 4</text>
      <text x="74" y="73">•  Weakness 1</text><text x="74" y="76.5">•  Weakness 2</text><text x="74" y="80">•  Weakness 3</text><text x="74" y="83.5">•  Weakness 4</text>
      <text x="117" y="73">•  Opportunities 1</text><text x="117" y="76.5">•  Opportunities 2</text><text x="117" y="80">•  Opportunities 3</text><text x="117" y="83.5">•  Opportunities 4</text>
      <text x="170" y="73">•  Threats 1</text><text x="170" y="76.5">•  Threats 2</text><text x="170" y="80">•  Threats 3</text><text x="170" y="83.5">•  Threats 4</text>
    </g>
  </svg></div><span class="num">23</span></div>

  <!-- 24 our partners -->
  <div class="cell"><div class="slide"><svg viewBox="0 0 219 124">
    <text x="18" y="16" class="ttl">OUR PARTNERS</text>
    <text x="18" y="22" class="sub">Add some summary text here to reinforce your points.</text>
    <g fill="none" stroke="var(--blue)" stroke-width=".7">
      <circle cx="33" cy="54" r="16"/><circle cx="97" cy="54" r="16"/><circle cx="161" cy="54" r="16"/>
      <circle cx="65" cy="86" r="16"/><circle cx="129" cy="86" r="16"/><circle cx="193" cy="86" r="16"/>
    </g>
  </svg></div><span class="num">24</span></div>

  <!-- 25 our clients -->
  <div class="cell"><div class="slide"><svg viewBox="0 0 219 124">
    <text x="18" y="16" class="ttl">OUR CLIENTS</text>
    <text x="18" y="22" class="sub">Add some summary text here to reinforce your points.</text>
    <g fill="none" stroke="var(--cyan)" stroke-width=".7">
      <circle cx="33" cy="54" r="16"/><circle cx="97" cy="54" r="16"/><circle cx="161" cy="54" r="16"/>
      <circle cx="65" cy="86" r="16"/><circle cx="129" cy="86" r="16"/><circle cx="193" cy="86" r="16"/>
    </g>
  </svg></div><span class="num">25</span></div>

  <!-- 26 our qualifications -->
  <div class="cell"><div class="slide"><svg viewBox="0 0 219 124">
    <text x="18" y="16" class="ttl">OUR QUALIFICATIONS</text>
    <text x="18" y="22" class="sub">Add some summary text here to reinforce your points.</text>
    <g fill="none" stroke="var(--blue)" stroke-width=".7">
      <circle cx="33" cy="54" r="16"/><circle cx="97" cy="54" r="16"/><circle cx="160" cy="54" r="16"/>
      <circle cx="65" cy="86" r="16"/><circle cx="129" cy="86" r="16"/><circle cx="192" cy="86" r="16"/>
    </g>
  </svg></div><span class="num">26</span></div>

  <!-- 27 our priorities -->
  <div class="cell"><div class="slide"><svg viewBox="0 0 219 124">
    <text x="18" y="16" class="ttl">OUR PRIORITIES</text>
    <text x="18" y="22" class="sub">Add some summary text here to reinforce your points.</text>
    <g fill="none" stroke-width=".9" stroke-linecap="round" stroke-linejoin="round">
      <path d="M23 41l7-5-2 7-1.5-2z" stroke="var(--cyan)"/>
      <path d="M23 65l1-3 4-4 2 2-4 4z" stroke="var(--cyan)"/>
      <path d="M23 80v3a3 3 0 0 0 6 0v-3M26 86v1a2 2 0 0 0 4 0v-1" stroke="var(--blue)"/>
      <rect x="23" y="101" width="7" height="7" rx="1" stroke="var(--blue)"/>
    </g>
    <g>
      <text x="37" y="36" class="tb" style="font-size:2.9px">PRIORITY 1</text><text x="37" y="40" class="tx">Add some summary text here</text><text x="37" y="43.5" class="tx">to reinforce your points.</text>
      <text x="37" y="57" class="tb" style="font-size:2.9px">PRIORITY 2</text><text x="37" y="61" class="tx">Add some summary text here</text><text x="37" y="64.5" class="tx">to reinforce your points.</text>
      <text x="37" y="79" class="tb" style="font-size:2.9px">PRIORITY 3</text><text x="37" y="83" class="tx">Add some summary text here</text><text x="37" y="86.5" class="tx">to reinforce your points.</text>
      <text x="37" y="100" class="tb" style="font-size:2.9px">PRIORITY 4</text><text x="37" y="104" class="tx">Add some summary text here</text><text x="37" y="107.5" class="tx">to reinforce your points.</text>
    </g>
    <polygon points="155,27 177,68 133,68" fill="var(--cyan)"/>
    <polygon points="133,68 177,68 155,109" fill="var(--cyan-soft)"/>
    <polygon points="133,68 155,109 111,109" fill="var(--blue)"/>
    <polygon points="177,68 199,109 155,109" fill="var(--sky)"/>
    <g fill="none" stroke="#fff" stroke-width=".9" stroke-linecap="round" stroke-linejoin="round">
      <path d="M150 58l9-6-3 9-2-2.5z"/>
      <path d="M151 86l2-4 5-4 1.5 1.5-4 5z"/>
      <rect x="129" y="93" width="8" height="8" rx="1"/><path d="M131.5 95v4M134.5 95v4M131.5 97h3"/>
      <path d="M173 92v3a3 3 0 0 0 6 0v-3M176 98v1a2 2 0 0 0 4 0v-1"/>
    </g>
  </svg></div><span class="num">27</span></div>

  <!-- 28 testimonial -->
  <div class="cell"><div class="slide"><svg viewBox="0 0 219 124">
    <rect role="img" aria-label="Soft photo of a healthcare professional, cyan tones" width="219" height="124" fill="url(#wash)"/>
    <text x="26" y="62" style="font-size:26px;font-weight:700;fill:#fff;opacity:.6">“</text>
    <text x="190" y="80" style="font-size:26px;font-weight:700;fill:#fff;opacity:.6">”</text>
    <text x="107" y="58" text-anchor="middle" style="font-size:7px;font-weight:600" class="white">Spot for a bold quote or</text>
    <text x="107" y="67" text-anchor="middle" style="font-size:7px;font-weight:600" class="white">testimonial here.</text>
    <text x="107" y="90" text-anchor="middle" style="font-size:3.7px;fill:#fff;opacity:.85">First Last Name</text>
    <text x="107" y="95" text-anchor="middle" style="font-size:3.7px;fill:#fff;opacity:.85">Company Name</text>
  </svg></div><span class="num">28</span></div>

  <!-- 29 faq -->
  <div class="cell"><div class="slide"><svg viewBox="0 0 219 124">
    <text x="20" y="21" class="ttl">FREQUENTLY ASKED QUESTIONS</text>
    <g fill="none" stroke="var(--blue)" stroke-width=".5">
      <circle cx="22" cy="37" r="2"/><circle cx="124" cy="37" r="2"/><circle cx="22" cy="79" r="2"/><circle cx="124" cy="79" r="2"/>
    </g>
    <g class="tb" style="font-size:2.4px">
      <text x="27" y="38">Insert a frequently asked question here?</text><text x="129" y="38">Insert a frequently asked question here?</text>
      <text x="27" y="80">Insert a frequently asked question here?</text><text x="129" y="80">Insert a frequently asked question here?</text>
    </g>
  </svg>
  <p class="para" style="left:27px;top:40px;width:70px">Give your answer here to the best of your ability. Could be long or short. Just answer the questions. Give your answer here to the best of your ability. Could be long or short. Just answer the questions.</p>
  <p class="para" style="left:129px;top:40px;width:70px">Give your answer here to the best of your ability. Could be long or short. Just answer the questions. Give your answer here to the best of your ability. Could be long or short. Just answer the questions.</p>
  <p class="para" style="left:27px;top:82px;width:70px">Give your answer here to the best of your ability. Could be long or short. Just answer the questions. Give your answer here to the best of your ability. Could be long or short. Just answer the questions.</p>
  <p class="para" style="left:129px;top:82px;width:70px">Give your answer here to the best of your ability. Could be long or short. Just answer the questions. Give your answer here to the best of your ability. Could be long or short. Just answer the questions.</p>
  </div><span class="num">29</span></div>

  <!-- 30 text-only slide -->
  <div class="cell"><div class="slide"><svg viewBox="0 0 219 124">
    <text x="20" y="16" class="ttl">TEXT-ONLY SLIDE</text>
  </svg>
  <div class="para cols" style="left:16px;top:28px;width:188px;column-count:3">Refers to a good or service being offered by a company. Ideally, a product should meet a certain consumer demand, or it should be so competing that consumers believe they need it. Business executives should have a plan for dealing with products at every stage of their life cycles. Marketers must link the price to the real and perceived value of the product. Place decisions outline where the product is sold and how it is delivered to the market. The goal of business executives is to get their products in front of the consumers who are most likely to buy them. Refers to a good or service being offered by a company. Ideally, a product should meet a certain consumer demand, or it should be so competing that consumers believe they need it. Business executives should have a plan for dealing with products at every stage of their life cycles. Marketers must link the price to the real and perceived value of the product, and also consider supply costs, seasonal discounts and prices used by competitors. Refers to a good or service being offered by a company. Ideally, a product should meet a certain consumer demand, or it should be so competing that consumers believe they need it. Business executives should have a plan for dealing with products at every stage of their life cycles.</div>
  </div><span class="num">30</span></div>

  <!-- 31 thank you -->
  <div class="cell"><div class="slide"><svg viewBox="0 0 219 124">
    <rect role="img" aria-label="Photo of medical technology workspace in cyan tones" width="219" height="124" fill="url(#wash)"/>
    <circle cx="109.5" cy="38" r="11" fill="none" stroke="#fff" stroke-opacity=".6" stroke-width=".6"/>
    <text x="109.5" y="37" text-anchor="middle" style="font-size:3.4px;fill:#fff;opacity:.75">YOUR</text>
    <text x="109.5" y="41" text-anchor="middle" style="font-size:3.4px;fill:#fff;opacity:.75">LOGO</text>
    <text x="109.5" y="83" text-anchor="middle" style="font-size:10px;font-weight:700" class="white">THANK YOU</text>
  </svg></div><span class="num">31</span></div>

</main>
</body>
</html>
```